Book Cover

Hello!
I need someone to design a book cover with the title, subtitle and one of the photos attached.

- Title: Beyond the Grey Hours - By Corwin Ashdale
- Subtitle: A Steady Handbook for finding calm and strength after hard news.

```html
<!DOCTYPE html>
<html lang="en">
<head>
<meta charset="utf-8">
<title>Beyond the Grey Hours – Book Cover</title>
<link rel="stylesheet" href="https://fonts.googleapis.com/css2?family=Roboto+Condensed:wght@300;400;700&family=Playfair+Display:ital@1&family=Montserrat:wght@500&display=swap">
<style>
  :root {
    --stage: #e6e6e6;
    --ink: #1c1c1c;
    --accent: #ef5f22;
    --sky-top: #dfeef8;
    --sky-mid: #eef2ee;
    --field: #cdb48a;
    --jacket: #2b4f9c;
    --jacket-deep: #1e3a78;
    --white: #ffffff;
  }
  * { margin: 0; padding: 0; box-sizing: border-box; }
  html, body {
    width: 1200px; height: 587px; overflow: hidden;
    background: var(--stage);
  }
  .stage {
    width: 1200px; height: 587px;
    display: flex; justify-content: center; align-items: center;
  }
  .cover {
    position: relative;
    width: 400px; height: 587px;
    overflow: hidden;
  }
  .cover-photo {
    position: absolute; inset: 0;
    background:
      radial-gradient(ellipse 70% 55% at 78% 92%, var(--jacket) 0%, var(--jacket-deep) 55%, transparent 75%),
      linear-gradient(180deg, var(--sky-top) 0%, var(--sky-mid) 35%, var(--field) 75%, #b89c70 100%);
  }
  .title {
    position: absolute; left: 0; right: 0; top: 14px;
    text-align: center;
    font-family: "Roboto Condensed", sans-serif;
    line-height: 1;
  }
  .title-light {
    display: block;
    font-weight: 300;
    font-size: 58px;
    color: var(--ink);
    letter-spacing: 1px;
  }
  .title-bold {
    display: block;
    margin-top: 4px;
    font-weight: 700;
    font-size: 56px;
    color: var(--accent);
  }
  .subtitle {
    position: absolute; left: 35px; top: 139px;
    width: 150px; height: 154px;
    padding-left: 9px;
    border-left: 1px solid var(--ink);
    font-family: "Montserrat", sans-serif;
    font-weight: 500;
    font-size: 14.5px;
    line-height: 19px;
    color: var(--ink);
  }
  .subtitle-lead { display: block; }
  .subtitle-script {
    display: block;
    font-family: "Playfair Display", serif;
    font-style: italic;
    font-size: 29px;
    line-height: 28px;
    color: var(--accent);
    margin: 2px 0 3px;
  }
  .subtitle-swash {
    position: absolute; left: 89px; top: 298px;
  }
  .author {
    position: absolute; left: 0; right: 0; top: 520px;
    text-align: center;
    font-family: "Roboto Condensed", sans-serif;
    font-weight: 400;
    font-size: 39px;
    color: var(--white);
    letter-spacing: 0.5px;
  }
</style>
</head>
<body>
<main class="stage">
  <section class="cover">
    <div class="cover-photo" role="img" aria-label="Portrait photo of the author standing outdoors in a blue jacket, with a soft-focus field of dry grass and pale sky behind him"></div>
    <h1 class="title">
      <span class="title-light">BEYOND THE</span>
      <span class="title-bold">GREY HOURS</span>
    </h1>
    <p class="subtitle">
      <span class="subtitle-lead">A</span>
      <span class="subtitle-script">Steady<br>Handbook</span>
      for finding calm and strength after hard news.
    </p>
    <svg class="subtitle-swash" width="70" height="24" viewBox="0 0 70 24" aria-hidden="true">
      <path d="M1 22 C 14 8, 38 1, 68 3" fill="none" stroke="#1c1c1c" stroke-width="1.3"/>
    </svg>
    <p class="author">CORWIN ASHDALE</p>
  </section>
</main>
</body>
</html>
```